New logo and packaging for Chicago based skincare company

Venmira needs a new logo and packaging to help in marketing our new anti-aging skincare line.

About Us
We're quirky, skin-obsessed beauty geeks with a knack for research and a love for all things skincare. Our ambition to create REAL products with exotic ingredients inspired the name Venmira which translates to peau + jolie meaning beautiful skin in french.

Our Products
We strive to do it differently. We develop high potency, natural skincare products using top of the line, novel ingredients imported from all over the globe. Our products are made in the USA and free from gluten, parabens, sulfates, and useless fillers that can't deliver.
Price range: $25-75 (moderate)

LOGO
Open to any color/typography except red and purple. Should also be: modern, feminine, cultured, neutral, vibrant, simple, timeless, and sophisticated

LABEL
Logo placed on label, but should not be the focal point of product. EGF SERUM should grab attention of quick glancers
The ideal label design pairs neutrals with brights while achieving balance between minimalism and complexity.
Incorporates some sort of unconventionality, boldness, or uniqueness without adding distraction.

Color: Mostly white or silver background with splash of color (no purple, light pinks, or red). See attached kraft color chart for direction. Bright blues (teal, cobalt, navy, sky blue, and greens are ideal)

Target Market(s)

Target audience: Socially and health conscious women, cultured, ages 25-60, seeks high quality natural products with effective ingredients.

Industry/Entity Type

Skin Care Product

Logo Text

Venmira

Font styles to use
Other font styles liked:
• Open

Colors
f6f6f6
ffffff
fdfdfd
eeeeee
fbfbfb
0255a3
3176b5
33a6d7
86cfc6

Requirements
Must have
• Packaging includes:
• 1 oz amber glass bottles with white dropper - see attached image
• Dimensions: 1.25" width by 4.1" height
• Label should wrap around bottle similar to peptide complex image and includes ingredient list; Logo should be not focal point of label
• Green (peptide complex) label shows ideal clarity
• "NuGlint" can be written in several different ways, feel free to get creative
• Label Text:
• EGF
• NUGLINT
• SERUM
• Anti-aging Skin firming Scar removal
• 1 FL OZ (30ml)
• Ingredients:
• Hamamelis Virginiana (Witch Hazel) Water, Aqua (Water), Alcohol, Glycerin, Polysorbate 20, rh-Oligopeptide-1(EGF), Caprooyl Tetrapeptide-3, Cocos Nucifera (Coconut) Fruit Juice, Lavandula Angustifolia (Lavender) Oil, Citrus
• Paradisi (Pink Grapefruit) Peel Oil*, Citrus Aurantium Dulcis (Orange) Peel Oil*, Santalum Austrocaledonicum (Sandalwood) Wood Oil, Boswellia Carterii (Frankincense) Oil, Rosa Damascena Flower Oil, Dextran, Xanthan Gum,
• Gluconolactone, Sodium Benzoate
• Directions:
• Apply a small amount of EGF serum to clean skin once or twice daily. Allow to dry. Can be used both morning and night, and under makeup. Follow with moisturizer.
• Caution: For external use only. Use only as directed. Avoid contact with eyes. If contact occurs, rinse well with water.
• Distributed by Venmira, LLC
• Munster, Indiana 46398
• Made in USA, FDA Registered lab (please use symbols for these)
Nice to have
• Either or: White space, silver, boldness, numbers, kraft colors (see attached) shapes, geometric patterns, minimalism
• Label: Incorporate shapes and dimensions with minimal/bare background
• Open to handwritten fonts if clear and easy to read
Should not have
• No more than 3-4 colors, look too busy, cursive fonts

```html
<!DOCTYPE html>
<html lang="en">
<head>
<meta charset="utf-8">
<title>Venmira — EGF NuGlint Serum Label</title>
<link rel="stylesheet" href="https://fonts.googleapis.com/css2?family=Jost:wght@300;400&family=Tinos:wght@400&display=swap">
<style>
  :root {
    --paper: #ffffff;
    --brand-orange: #e9965e;
    --brand-orange-deep: #e8904f;
    --brand-peach: #f6c9a8;
    --label-ink: #ffffff;
  }
  * { box-sizing: border-box; margin: 0; padding: 0; }
  html, body {
    width: 1200px;
    height: 689px;
    overflow: hidden;
    background: var(--paper);
  }
  .canvas {
    position: relative;
    width: 1200px;
    height: 689px;
    background: var(--paper);
  }

  /* Primary wordmark */
  .wordmark {
    position: absolute;
    left: 383px;
    top: 60px;
    width: 700px;
    text-align: center;
    font-family: "Jost", sans-serif;
    font-weight: 300;
    font-size: 190px;
    line-height: 1;
    letter-spacing: 2px;
    color: var(--brand-orange);
  }

  /* Flat wrap label */
  .label {
    position: absolute;
    left: 409px;
    top: 426px;
    width: 678px;
    height: 211px;
    overflow: hidden;
    background: linear-gradient(90deg,
      var(--brand-orange-deep) 0%,
      var(--brand-orange) 40%,
      var(--brand-orange) 62%,
      var(--brand-peach) 100%);
    color: var(--label-ink);
  }
  .label__badge {
    position: absolute;
    left: 256px;
    top: -86px;
    width: 166px;
    height: 172px;
    border-radius: 50%;
    background: var(--paper);
  }
  .label__logo {
    position: absolute;
    left: 256px;
    top: 18px;
    width: 166px;
    text-align: center;
    font-family: "Jost", sans-serif;
    font-weight: 300;
    font-size: 30px;
    line-height: 1;
    color: var(--brand-orange);
  }

  .label__copy {
    position: absolute;
    font-family: "Tinos", serif;
    text-align: center;
    font-size: 8.4px;
    line-height: 1.3;
  }
  .label__directions { left: 20px; top: 30px; width: 220px; }
  .label__caution { left: 20px; top: 78px; width: 220px; }
  .label__heading { text-transform: uppercase; }
  .label__ingredients { left: 465px; top: 13px; width: 200px; line-height: 1.22; }

  .label__claims {
    position: absolute;
    left: 189px;
    top: 90px;
    width: 300px;
    text-align: center;
    font-family: "Tinos", serif;
    font-size: 11.5px;
    line-height: 1.45;
  }
  .label__product {
    position: absolute;
    left: 239px;
    top: 126px;
    width: 200px;
    text-align: center;
    font-family: "Tinos", serif;
    font-size: 17px;
    line-height: 0.95;
    letter-spacing: 0.3px;
  }
  .label__volume {
    position: absolute;
    left: 287px;
    top: 188px;
    width: 104px;
    height: 30px;
    border-radius: 50%;
    background: var(--paper);
    color: var(--brand-orange);
    font-family: "Tinos", serif;
    font-size: 9.5px;
    text-align: center;
    padding-top: 6px;
  }
</style>
</head>
<body>
<main class="canvas">
  <div class="wordmark">Venmira</div>

  <section class="label" aria-label="Wrap-around bottle label">
    <div class="label__badge"></div>
    <div class="label__logo">Venmira</div>

    <div class="label__copy label__directions">
      <p class="label__heading">Directions:</p>
      <p>Apply a small amount of EGF serum to clean skin once or twice daily. Allow to dry. Can be used both morning and night, and under makeup. Follow with moisturizer.</p>
    </div>

    <div class="label__copy label__caution">
      <p class="label__heading">Caution:</p>
      <p>For external use only. Use only as directed. Avoid contact with eyes. If contact occurs, rinse well with water.</p>
    </div>

    <div class="label__claims">
      <p>Anti-aging Skin</p>
      <p>firming Cell renewal Scar removal</p>
    </div>

    <div class="label__product">
      <p>EGF</p>
      <p>NuGLINT</p>
      <p>SERUM</p>
    </div>

    <div class="label__volume">1 FL OZ (30ml)</div>

    <div class="label__copy label__ingredients">
      <p class="label__heading">Ingredients:</p>
      <p>Hamamelis Virginiana (Witch Hazel) Water, Aqua (Water), Alcohol, Glycerin, Polysorbate 20, rh-Oligopeptide-1 (EGF), Caprooyl Tetrapeptide-3, Cocos Nucifera (Coconut) Fruit Juice, Lavandula Angustifolia (Lavender) Oil, Citrus Paradisi (Pink Grapefruit) Peel Oil*, Citrus Aurantium Dulcis (Orange) Peel Oil*, Santalum Austrocaledonicum (Sandalwood) Wood Oil, Boswellia Carterii (Frankincense) Oil, Rosa Damascena Flower Oil, Dextran, Xanthan Gum, Gluconolactone, Sodium Benzoate</p>
    </div>
  </section>
</main>
</body>
</html>
```